Socialio landing page design

We are a Video Production Company and plan to launch our Business Fan Page soon. We are running a competition and need a design done for the related Socialio landing page.

The landing page should have the following copy:

Win a Web Video Advertisement Worth $4000!
To enter you must:
1. Vote for the web video advertisement that you enjoy the most (check out the Poll Tab)
2. "Like" our Socialio Fan Page
3. Explain what an ideal web video advertisement would look like for your business (Post this on our wall)
Conditions apply so check out the Poll tab for more information. Competition ends June 30th so get voting!

I have included some previous marketing material for reference only. You do not need to use this as a style a guide

Target Market(s)

Business owners or marketing managers

Requirements
Must have
• Lumora Reel-works Logo
web address included: www.lumorarw.example
An image needs to accompany the copy
Should not have
• text only

```html
<!DOCTYPE html>
<html lang="en">
<head>
<meta charset="utf-8">
<title>Lumora Reel-works – Win a Web Video Advertisement</title>
<link rel="stylesheet" href="https://fonts.googleapis.com/css2?family=Archivo+Black&family=Roboto+Condensed:wght@400;700&family=Roboto:wght@400;700&display=swap">
<style>
:root{
  --navy:#0b3f78;
  --deep:#08305e;
  --blue:#1d7fd0;
  --sky:#58b6f0;
  --pale:#dff1fd;
  --white:#ffffff;
  --orange:#f07a12;
  --orange-dark:#d25a06;
  --red:#e8231b;
  --text:#1d2430;
}
*{box-sizing:border-box;margin:0;padding:0}
html,body{width:847px;height:1200px;overflow:hidden}
body{background:#eef6fc;font-family:"Roboto",Arial,sans-serif;color:var(--text)}
.page{position:relative;width:847px;height:1200px;overflow:hidden;
  background:linear-gradient(180deg,#bfe3fa 0%,#7fc6f2 34%,#a9dbf8 70%,#d9effc 100%)}

/* like band (behind hero so the callout can overlap it) */
.like-band{position:absolute;left:0;top:398px;width:847px;height:108px;
  background:linear-gradient(180deg,#4aa7e6 0%,#7cc5f3 100%)}
.like-text{position:absolute;right:265px;top:437px;font-family:"Roboto Condensed",Arial,sans-serif;
  font-size:29px;line-height:36px;color:var(--white);white-space:nowrap}
.like-button{position:absolute;left:603px;top:418px;width:192px;height:72px;background:#3b5c9c;
  border:2px solid var(--white);border-radius:4px;display:flex;align-items:center;justify-content:center;
  font-family:"Roboto Condensed",Arial,sans-serif;font-weight:700;font-size:28px;color:var(--white)}

/* hero */
.hero{position:absolute;left:0;top:0;width:847px;height:398px;background:var(--white);z-index:2}
.hero-clip{position:absolute;inset:0;overflow:hidden}
.hero-photo{position:absolute;left:0;top:0;width:470px;height:398px;
  background:linear-gradient(120deg,#e7edf2 0%,#cfd9e2 45%,#b9c8d6 100%)}
.hero-stripes{position:absolute;left:0;top:0;width:847px;height:398px}
.hero-title{position:absolute;left:650px;top:175px;width:420px;
  font-family:"Archivo Black",Arial,sans-serif;font-size:56px;line-height:.92;
  color:var(--navy);text-transform:uppercase;text-align:center;
  transform:translate(-50%,-50%) rotate(38deg);transform-origin:center;
  text-shadow:3px 3px 0 var(--white)}
.reel{position:absolute;left:425px;top:268px;width:115px;height:115px;border-radius:50%;
  background:radial-gradient(circle,#f4f4f4 0%,#9da3a8 70%,#5d6368 100%)}
.callout{position:absolute;left:88px;top:250px;width:330px;height:138px;
  background:var(--white);border-radius:12px;box-shadow:0 3px 8px rgba(0,0,0,.25);
  transform:rotate(-16deg);padding:14px 18px;
  font-family:"Roboto Condensed",Arial,sans-serif;font-weight:700;text-transform:uppercase;color:var(--blue)}
.callout-lead{font-size:21px;line-height:1.05}
.callout-label{font-size:17px;margin-top:4px}
.callout-phone{font-size:34px;line-height:1.05;color:var(--orange)}

/* brand */
.brand{position:absolute;left:675px;top:10px;width:160px;height:104px;background:var(--white);
  border:3px solid var(--blue);border-radius:8px;display:flex;flex-direction:column;
  align-items:center;justify-content:center;gap:6px}
.brand-mark{width:18px;height:18px;background:var(--blue);border-radius:50%}
.brand-name{font-family:"Roboto Condensed",Arial,sans-serif;font-weight:700;font-size:19px;color:var(--blue)}

/* contest panel */
.contest{position:absolute;left:35px;top:505px;width:777px;height:425px;border-radius:22px;
  background:linear-gradient(180deg,#1f6fb8 0%,#3f95d8 30%,#bfe2f8 100%);padding:14px}
.contest-inner{width:100%;height:100%;border-radius:16px;
  background:linear-gradient(180deg,#7cc2ef 0%,#cde9fb 45%,#ffffff 100%);position:relative}
.contest-title{position:absolute;left:27px;top:21px;width:695px;height:86px;border-radius:18px;
  background:linear-gradient(180deg,#ff9a33 0%,var(--orange) 50%,var(--orange-dark) 100%);
  border:2px solid var(--white);display:flex;align-items:center;justify-content:center;
  font-family:"Roboto Condensed",Arial,sans-serif;font-weight:700;font-size:31px;color:var(--white);text-transform:uppercase}
.steps{position:absolute;left:40px;top:143px;width:640px;list-style:none}
.step{position:relative;padding-left:44px;margin-bottom:26px;
  font-family:"Roboto Condensed",Arial,sans-serif;font-weight:700;font-size:22px;line-height:1.3;
  color:var(--deep);text-transform:uppercase}
.step svg{position:absolute;left:0;top:3px;width:26px;height:26px}

/* closing */
.conditions{position:absolute;left:76px;top:950px;width:372px;font-size:19.5px;line-height:1.4;color:var(--navy)}
.conditions .date{color:var(--red)}
.poll-button{position:absolute;left:480px;top:950px;width:318px;height:76px;border-radius:38px;
  background:linear-gradient(180deg,#2a6bb3 0%,var(--deep) 100%);border:3px solid #9fd1f5;
  display:flex;align-items:center;justify-content:center;gap:18px;
  font-family:"Archivo Black",Arial,sans-serif;font-size:30px;color:var(--white);text-transform:uppercase;
  box-shadow:0 3px 6px rgba(0,0,0,.3)}
.poll-button svg{width:40px;height:40px}

/* footer */
.footer{position:absolute;left:13px;top:1066px;width:823px;height:124px;
  background:linear-gradient(180deg,#5fb9ef 0%,#bfe5fb 100%);border:2px solid #e8f6ff}
.social{position:absolute;left:242px;top:28px;display:flex;gap:12px}
.social span{width:46px;height:46px;border-radius:6px;background:var(--navy);display:block}
.social span:nth-child(2){background:#2a79b8}
.social span:nth-child(3){background:#39a4dc}
.social span:nth-child(4){background:#3f9a52}
.social span:nth-child(5){background:#e45fa1}
.social span:nth-child(6){background:#6f7c86}
.copyright{position:absolute;left:0;top:94px;width:100%;text-align:center;font-size:15px;color:var(--text)}
</style>
</head>
<body>
<main class="page">
  <section class="like-band"></section>
  <p class="like-text">Like our Socialio fan page</p>
  <div class="like-button">Socialio</div>

  <header class="hero">
    <div class="hero-clip">
      <div class="hero-photo" role="img" aria-label="Photo of a woman shouting into a red and white megaphone"></div>
      <svg class="hero-stripes" viewBox="0 0 847 398" aria-hidden="true">
        <polygon points="470,0 640,0 847,240 847,398 760,398 470,120" fill="#f7941d"/>
        <polygon points="500,0 847,0 847,398 800,398 500,60" fill="#1d7fd0"/>
        <polygon points="560,0 847,0 847,330 560,30" fill="#3c9be3"/>
      </svg>
      <div class="hero-title">Get your message through</div>
    </div>
    <div class="reel" role="img" aria-label="Illustration of a film reel"></div>
    <div class="callout">
      <p class="callout-lead">Our creative team is waiting for your call</p>
      <p class="callout-label">Call now on:</p>
      <p class="callout-phone">02 5550 1234</p>
    </div>
    <div class="brand">
      <span class="brand-mark"></span>
      <span class="brand-name">Lumora Reel-works</span>
    </div>
  </header>

  <section class="contest">
    <div class="contest-inner">
      <h1 class="contest-title">Win a web video advertisement worth $4000!</h1>
      <ol class="steps">
        <li class="step"><svg viewBox="0 0 26 26"><circle cx="13" cy="13" r="11" fill="none" stroke="#08305e" stroke-width="2.5"/><path d="M7 13h11M13 8l5 5-5 5" fill="none" stroke="#08305e" stroke-width="2.5"/></svg>Vote for the web video advertisement that you enjoy the most (check out the poll tab)</li>
        <li class="step"><svg viewBox="0 0 26 26"><circle cx="13" cy="13" r="11" fill="none" stroke="#08305e" stroke-width="2.5"/><path d="M7 13h11M13 8l5 5-5 5" fill="none" stroke="#08305e" stroke-width="2.5"/></svg>"Like" our Socialio fan page</li>
        <li class="step"><svg viewBox="0 0 26 26"><circle cx="13" cy="13" r="11" fill="none" stroke="#08305e" stroke-width="2.5"/><path d="M7 13h11M13 8l5 5-5 5" fill="none" stroke="#08305e" stroke-width="2.5"/></svg>Explain what an ideal web video advertisement would look like for your business (post this on our wall)</li>
      </ol>
    </div>
  </section>

  <p class="conditions">Conditions apply so check out the Poll tab for more information. Competition ends <span class="date">June 30th</span> so get voting!</p>
  <a class="poll-button">Your poll
    <svg viewBox="0 0 40 40"><circle cx="20" cy="20" r="16" fill="none" stroke="#fff" stroke-width="3"/><path d="M11 20h16M20 12l8 8-8 8" fill="none" stroke="#fff" stroke-width="3.5"/></svg>
  </a>

  <footer class="footer">
    <div class="social"><span></span><span></span><span></span><span></span><span></span><span></span></div>
    <p class="copyright">©2011, Copyright, All Rights Reserved, www.lumorarw.example</p>
  </footer>
</main>
</body>
</html>
```